M Website

We need a website design for a construction plant company. You may use a combination of our photos and the stock images. See the logo for company colours. It also be of great value to see moving pictures like the ones on the link: https://www.bellwickventures.co.za/copy-of-about-us. See our uploaded files for content.

Target Market(s)

Construction

Number of Pages Required

5+ page

```html
<!DOCTYPE html>
<html lang="en">
<head>
<meta charset="utf-8">
<title>K4 Logistic &amp; Plant Hire</title>
<link href="https://fonts.googleapis.com/css2?family=Roboto:wght@400;500;700;900&display=swap" rel="stylesheet">
<style>
:root{
  --yellow:#f2a81d;
  --yellow-dark:#e39a0c;
  --dark:#262626;
  --ink:#2b2b2b;
  --muted:#666;
  --grey-bg:#f4f4f4;
  --field:#f2f2f2;
  --white:#fff;
}
*{box-sizing:border-box;margin:0;padding:0}
html,body{width:1200px;height:3956px;overflow:hidden}
body{position:relative;background:var(--white);font-family:'Roboto',sans-serif;color:var(--ink)}
.abs{position:absolute}
.btn{position:absolute;background:var(--yellow);color:#fff;border-radius:22px;font-size:15px;display:flex;align-items:center;justify-content:center;font-weight:500}
.section-title{position:absolute;font-size:32px;font-weight:500;color:var(--ink);text-align:center;width:1200px;left:0}

/* top bar */
.topbar{left:0;top:0;width:1200px;height:37px;background:var(--dark);color:#ddd;font-size:14px}
.topbar span{position:absolute;top:10px}
.social-sq{position:absolute;top:0;width:37px;height:37px}

/* header */
.header{left:0;top:37px;width:1200px;height:113px;background:#fff}
.brand{position:absolute;left:78px;top:20px;display:flex;align-items:center;gap:10px}
.brand-mark{width:22px;height:22px;background:var(--yellow);border-radius:50%}
.brand-name{font-size:20px;font-weight:700;color:var(--ink);line-height:1.1}
.nav a{position:absolute;top:52px;font-size:15px;color:#444;text-decoration:none}
.nav .active{color:var(--yellow)}
.nav-underline{position:absolute;left:532px;top:108px;width:46px;height:5px;background:var(--yellow)}

/* hero */
.hero-photo{left:0;top:150px;width:1200px;height:510px;background:linear-gradient(180deg,#8d8a84 0%,#6f6a60 45%,#3c3a36 100%)}
.hero-title{left:440px;top:390px;font-size:52px;font-weight:700;color:#fff;line-height:1.05}

/* about */
.about-title{left:124px;top:766px;font-size:32px;font-weight:500}
.about-sub{left:124px;top:834px;font-size:14px;color:#333}
.about-text{left:124px;top:864px;width:480px;font-size:14px;line-height:1.5;color:#444}
.values li{position:absolute;list-style:none;font-size:15px;color:#444;padding-left:26px}
.values li::before{content:"";position:absolute;left:0;top:4px;border-left:12px solid #333;border-top:6px solid transparent;border-bottom:6px solid transparent}
.values li.on{color:var(--yellow)}
.values li.on::before{border-left-color:var(--yellow)}

/* services */
.services-bg{left:0;top:1187px;width:1200px;height:474px;background:var(--grey-bg)}
.card{position:absolute;top:1292px;width:243px;height:285px;background:#fff}
.card .ph{height:145px}
.card h3{font-size:15px;font-weight:500;text-align:center;margin-top:24px}
.card .rule{width:50px;height:3px;background:var(--yellow);margin:10px auto 14px}
.card p{font-size:12px;line-height:1.4;color:#444;text-align:center;padding:0 18px}
.plus{position:absolute;right:0;bottom:0;width:32px;height:32px;background:var(--yellow);color:#fff;font-size:24px;font-weight:700;display:flex;align-items:center;justify-content:center}

/* projects */
.tabs span{position:absolute;top:1780px;font-size:14px;color:#444}
.tabs .on{color:var(--yellow)}
.proj{position:absolute;top:1841px;width:244px;height:295px}

/* news & testimonials */
.nt-bg{left:0;top:2300px;width:1200px;height:495px;background:var(--grey-bg)}
.news{position:absolute;left:79px;width:454px;height:156px;background:#fff}
.news .ph{position:absolute;left:8px;top:8px;width:158px;height:140px}
.news h4{position:absolute;left:183px;top:14px;font-size:17px;font-weight:500}
.news .meta{position:absolute;left:183px;top:42px;width:255px;font-size:12px;color:var(--yellow);display:flex;justify-content:space-between}
.news .meta b{color:#333;font-weight:500}
.news p{position:absolute;left:183px;top:64px;width:240px;font-size:12px;line-height:1.4;color:#444}
.testi{position:absolute;left:662px;top:2452px;width:364px;height:272px;background:#fff;text-align:center}
.avatar{position:absolute;left:790px;top:2424px;width:108px;height:108px;border-radius:50%;background:radial-gradient(circle at 50% 40%,#9b9b9b,#5a5a5a);border:5px solid #fff}

/* clients */
.client{position:absolute;top:2938px;width:182px;height:126px;background:#f1f1f1;display:flex;align-items:center;justify-content:center;font-size:22px;font-weight:700;color:#333}
.dots{position:absolute;display:flex;gap:5px}
.dots i{width:7px;height:7px;border-radius:50%;background:#bbb;display:block}
.dots i.on{background:var(--yellow)}

/* contact */
.field{position:absolute;background:var(--field);font-size:13px;color:#666;padding:14px 16px}
.heading-left{position:absolute;font-size:32px;font-weight:500}
.heading-rule{position:absolute;height:3px;background:var(--yellow)}

/* footer */
.footer{left:0;top:3560px;width:1200px;height:396px;background:var(--dark);color:#fff}
.footer h5{position:absolute;font-size:18px;font-weight:500}
.footer ul{position:absolute;list-style:none;font-size:13px;line-height:19px}
.footer ul li::before{content:"• ";}
.qc{position:absolute;font-size:13px;line-height:18px;padding-left:24px}
.qc svg{position:absolute;left:0;top:2px}
</style>
</head>
<body>

<!-- Top bar -->
<div class="abs topbar">
  <span style="left:80px;display:flex;align-items:center;gap:8px;top:11px"><i style="display:block;width:20px;height:13px;background:#c9c9c9"></i>English ▾</span>
  <span style="left:440px;display:flex;align-items:center;gap:6px">
    <svg width="16" height="12" viewBox="0 0 16 12"><rect x="0.5" y="0.5" width="15" height="11" fill="none" stroke="#ddd"/><path d="M1 1l7 6 7-6" fill="none" stroke="#ddd"/></svg>info@k4plant.com</span>
  <span style="left:612px;display:flex;align-items:center;gap:6px">
    <svg width="14" height="14" viewBox="0 0 14 14"><path d="M3 1l2 3-1.5 1.5c.8 1.8 2.2 3.2 4 4L9 8l3 2-1 3C6 13 1 8 1 3z" fill="none" stroke="#ddd"/></svg>000 555 777 999</span>
  <div class="social-sq" style="left:947px;background:var(--yellow)"></div>
  <div class="social-sq" style="left:996px;width:14px;height:14px;top:12px;background:#ddd;border-radius:50%"></div>
  <div class="social-sq" style="left:1033px;width:14px;height:14px;top:12px;background:#ddd;border-radius:50%"></div>
  <div class="social-sq" style="left:1070px;width:14px;height:14px;top:12px;background:#ddd;border-radius:50%"></div>
  <div class="social-sq" style="left:1107px;width:14px;height:14px;top:12px;background:#ddd;border-radius:50%"></div>
</div>

<!-- Header -->
<header class="abs header">
  <div class="brand"><div class="brand-mark"></div><div class="brand-name">K4<br><span style="font-size:11px;font-weight:500">Logistic &amp; Plant Hire</span></div></div>
  <nav class="nav">
    <a class="active" style="left:536px">Home</a>
    <a style="left:618px">About us</a>
    <a style="left:718px">Services</a>
    <a style="left:812px">Projects</a>
    <a style="left:906px">Our Team</a>
    <a style="left:1006px">Contact us</a>
    <svg style="position:absolute;left:1107px;top:55px" width="14" height="14" viewBox="0 0 14 14"><circle cx="6" cy="6" r="4.5" fill="none" stroke="#777" stroke-width="1.5"/><path d="M9.5 9.5l3.5 3.5" stroke="#777" stroke-width="1.5"/></svg>
  </nav>
  <div class="nav-underline"></div>
</header>

<!-- Hero -->
<div class="abs hero-photo" role="img" aria-label="Two yellow backhoe loaders on a low-bed trailer"></div>
<div class="abs hero-title">K4<br>Construction</div>
<div class="btn" style="left:515px;top:497px;width:176px;height:40px">Read More</div>
<svg class="abs" style="left:0;top:540px" width="1200" height="130" viewBox="0 0 1200 130">
  <path d="M0 130 L0 95 Q600 150 1200 40 L1200 130 Z" fill="#fff"/>
  <path d="M0 95 Q600 150 1200 40 L1200 60 Q600 170 0 118 Z" fill="var(--yellow)"/>
</svg>

<!-- About -->
<h2 class="abs about-title">About us</h2>
<div class="abs about-sub">What is Lorem Ipsum?</div>
<p class="abs about-text">Lorem Ipsum is simply dummy text of the printing and typesetting dummy industry. Lorem Ipsum has been the industry's standard dummy text Ipsum in the ever since the 1500s.</p>
<ul class="values">
  <li class="on" style="left:124px;top:944px">Integrity</li>
  <li style="left:264px;top:944px">Accountability</li>
  <li style="left:124px;top:973px">Capability</li>
  <li style="left:264px;top:973px">Adaptability</li>
  <li style="left:124px;top:1004px">Ethics</li>
</ul>
<div class="btn" style="left:121px;top:1052px;width:177px;height:42px">Read More</div>
<div class="abs" style="left:646px;top:770px;width:422px;height:311px;background:var(--yellow)"></div>
<div class="abs" role="img" aria-label="Dump truck tipping soil on a site, video still" style="left:659px;top:786px;width:422px;height:308px;background:linear-gradient(180deg,#6d7f92 0%,#8d8c80 50%,#5b5346 100%)"></div>
<svg class="abs" style="left:850px;top:920px" width="40" height="40" viewBox="0 0 40 40"><circle cx="20" cy="20" r="18" fill="rgba(255,255,255,.85)"/><path d="M16 12l12 8-12 8z" fill="#444"/></svg>

<!-- Services -->
<div class="abs services-bg"></div>
<h2 class="section-title" style="top:1222px">Our Serices</h2>
<div class="card" style="left:79px"><div class="ph" role="img" aria-label="Road and stormwater works" style="background:linear-gradient(160deg,#8b8b83,#4d5047)"></div><h3>Roads &amp; Stormwater</h3><div class="rule"></div><p>Lorem Ipsum is simply dummy text of the printing and typesetting industry is simply dummy text</p><div class="plus">+</div></div>
<div class="card" style="left:345px"><div class="ph" role="img" aria-label="Water pipe laid in a trench" style="background:linear-gradient(160deg,#b08a5c,#6d5236)"></div><h3>Water Infrastructure</h3><div class="rule"></div><p>Lorem Ipsum is simply dummy text of the printing and typesetting industry is simply dummy text</p><div class="plus">+</div></div>
<div class="card" style="left:611px"><div class="ph" role="img" aria-label="Worker installing sanitation pipework" style="background:linear-gradient(160deg,#a89b86,#5e574b)"></div><h3>Sanitation Infrastructure</h3><div class="rule"></div><p>Lorem Ipsum is simply dummy text of the printing and typesetting industry is simply dummy text</p><div class="plus">+</div></div>
<div class="card" style="left:877px"><div class="ph" role="img" aria-label="New housing under construction" style="background:linear-gradient(180deg,#9eb2c6,#c9c2b4)"></div><h3>Housing</h3><div class="rule"></div><p>Lorem Ipsum is simply dummy text of the printing and typesetting industry is simply dummy text</p><div class="plus">+</div></div>

<!-- Projects -->
<h2 class="section-title" style="top:1723px">Our Projects</h2>
<div class="tabs">
  <span class="on" style="left:276px">ALL</span>
  <div class="abs" style="left:274px;top:1800px;width:30px;height:2px;background:var(--yellow)"></div>
  <span style="left:334px">Roads &amp; Stormwater</span>
  <span style="left:506px">Water Infrastructure</span>
  <span style="left:673px">Sanitation Infrastructure</span>
  <span style="left:869px">Housing</span>
</div>
<div class="proj" style="left:79px" role="img" aria-label="Paving machine with workers in high-visibility vests" style="background:#555"></div>
<div class="proj" style="left:79px;background:linear-gradient(180deg,#6f8fb6,#3a3a3a)" role="img" aria-label="Paving machine with workers"></div>
<div class="proj" style="left:345px;background:linear-gradient(180deg,#b9b4a8,#2f2f2f)" role="img" aria-label="Asphalt paver laying a road"></div>
<div class="proj" style="left:611px;background:linear-gradient(180deg,#7d8f6a,#3c3d3e)" role="img" aria-label="Road roller compacting asphalt"></div>
<div class="proj" style="left:877px;background:linear-gradient(180deg,#c7b48a,#8a5a2a)" role="img" aria-label="Yellow loader on a dirt site"></div>
<div class="btn" style="left:520px;top:2189px;width:176px;height:40px">View More</div>

<!-- News & Testimonials -->
<div class="abs nt-bg"></div>
<h2 class="heading-left" style="left:79px;top:2350px;font-size:28px">News &amp; Career</h2>
<svg class="abs" style="left:518px;top:2355px" width="14" height="26" viewBox="0 0 14 26"><path d="M2 8l5-5 5 5M2 18l5 5 5-5" fill="none" stroke="#555" stroke-width="1.6"/></svg>
<div class="news" style="top:2405px"><div class="ph" role="img" aria-label="Excavator at work" style="background:linear-gradient(160deg,#c9874a,#5d4a3a)"></div><h4>News Heading 01</h4><div class="meta"><span><b>By:</b> Lee Morgan</span><b>May 8th, 2018</b></div><p>Lorem Ipsum is simply dummy text of printing and typesetting industry.</p><div class="plus" style="width:28px;height:28px;font-size:20px">+</div></div>
<div class="news" style="top:2576px"><div class="ph" role="img" aria-label="Building towers against a bright sun" style="background:linear-gradient(160deg,#f3f0e2,#6b7f98)"></div><h4>News Heading 02</h4><div class="meta"><span><b>By:</b> Lee Morgan</span><b>May 8th, 2018</b></div><p>Lorem Ipsum is simply dummy text of printing and typesetting industry.</p><div class="plus" style="width:28px;height:28px;font-size:20px">+</div></div>

<h2 class="abs" style="left:662px;width:364px;text-align:center;top:2350px;font-size:28px;font-weight:500">Testimonials</h2>
<div class="testi">
  <div style="position:absolute;top:88px;width:100%;font-size:13px;font-weight:500">DANIEL HART</div>
  <div style="position:absolute;top:106px;width:100%;font-size:11px;color:var(--yellow)">Creative Director</div>
  <div style="position:absolute;top:130px;left:36px;font-size:34px;font-weight:700;line-height:1">“</div>
  <p style="position:absolute;top:138px;left:50px;width:264px;font-size:12px;line-height:1.45;font-weight:500">Lorem Ipsum simply dummy text of the printing and typesetting industry orem Ipsum has been the Lorem.</p>
  <div style="position:absolute;top:176px;right:36px;font-size:34px;font-weight:700;line-height:1">”</div>
  <div style="position:absolute;top:194px;width:100%;color:var(--yellow);font-size:12px;letter-spacing:1px">★★★★★</div>
  <div class="dots" style="left:164px;top:216px"><i class="on" style="width:5px;height:5px"></i><i style="width:5px;height:5px"></i><i style="width:5px;height:5px"></i></div>
</div>
<div class="avatar" role="img" aria-label="Portrait of the reviewer"></div>

<!-- Clients -->
<h2 class="section-title" style="top:2866px">Our Clients</h2>
<div class="client" style="left:119px;width:179px">Orbitline</div>
<div class="client" style="left:311px">Groundwell</div>
<div class="client" style="left:509px">Ironpath</div>
<div class="client" style="left:704px">Clearfield</div>
<div class="client" style="left:899px">Northbay</div>
<div class="dots" style="left:588px;top:3094px"><i class="on"></i><i></i><i></i></div>

<!-- Contact -->
<h2 class="heading-left" style="left:79px;top:3137px">Contact us</h2>
<div class="heading-rule" style="left:79px;top:3193px;width:100px"></div>
<div class="field" style="left:79px;top:3233px;width:253px;height:42px">First Name*</div>
<div class="field" style="left:348px;top:3233px;width:253px;height:42px">Last Name*</div>
<div class="field" style="left:79px;top:3294px;width:253px;height:42px">Phone*</div>
<div class="field" style="left:348px;top:3294px;width:253px;height:42px">Email*</div>
<div class="field" style="left:79px;top:3352px;width:522px;height:118px">Message</div>
<div class="btn" style="left:425px;top:3489px;width:176px;height:40px">Submit</div>

<h2 class="heading-left" style="left:638px;top:3137px">Map</h2>
<div class="abs" style="left:646px;top:3191px;width:422px;height:330px;background:var(--yellow)"></div>
<div class="abs" role="img" aria-label="Map of the United States with a location pin" style="left:659px;top:3207px;width:422px;height:327px;background:linear-gradient(135deg,#dfe8d4,#c9d8b9 55%,#b7cfe6)"></div>

<!-- Footer -->
<svg class="abs" style="left:0;top:3470px" width="1200" height="100" viewBox="0 0 1200 100">
  <path d="M0 60 Q700 110 1200 20 L1200 100 L0 100 Z" fill="var(--yellow)"/>
  <path d="M0 78 Q700 120 1200 45 L1200 100 L0 100 Z" fill="var(--dark)"/>
</svg>
<footer class="abs footer">
  <div class="brand" style="left:66px;top:96px"><div class="brand-mark"></div><div class="brand-name" style="color:#fff">K4<br><span style="font-size:11px;font-weight:500">Logistic &amp; Plant Hire</span></div></div>
  <p class="abs" style="left:66px;top:200px;width:290px;font-size:13px;line-height:1.4;font-weight:500">Lorem Ipsum is simply dummy text of the printing and typesetting industry. Lorem Ipsum has been the industry's standard dummy text ever since the 1500s,</p>
  <div class="abs" style="left:66px;top:276px;font-size:13px;font-weight:500">Read More ⊕</div>

  <h5 style="left:406px;top:118px">Quick Link</h5>
  <ul style="left:412px;top:176px"><li>Home</li><li>About</li><li>Services</li><li>Projects</li><li>Blogs</li><li>Contact Us</li></ul>

  <h5 style="left:612px;top:118px">Quick Contact</h5>
  <div class="qc" style="left:612px;top:168px"><svg width="12" height="14" viewBox="0 0 12 14"><path d="M6 13C2 8 1 6 1 5a5 5 0 0110 0c0 1-1 3-5 8z" fill="#fff"/></svg>418 Ridgeway Ave.<br>Stonebrook City, USA<br>TX 12345</div>
  <div class="qc" style="left:612px;top:226px"><svg width="12" height="12" viewBox="0 0 14 14"><path d="M3 1l2 3-1.5 1.5c.8 1.8 2.2 3.2 4 4L9 8l3 2-1 3C6 13 1 8 1 3z" fill="#fff"/></svg>00 987 654 3210</div>
  <div class="qc" style="left:612px;top:248px"><svg width="12" height="12" viewBox="0 0 14 14"><path d="M3 1l2 3-1.5 1.5c.8 1.8 2.2 3.2 4 4L9 8l3 2-1 3C6 13 1 8 1 3z" fill="#fff"/></svg>00 987 654 3210</div>
  <div class="qc" style="left:612px;top:270px"><svg width="13" height="10" viewBox="0 0 16 12"><rect width="16" height="12" fill="#fff"/><path d="M0 0l8 7 8-7" fill="none" stroke="#262626"/></svg>info@k4plant.com</div>

  <h5 style="left:894px;top:118px">Subscribe</h5>
  <div class="abs" style="left:894px;top:182px;font-size:13px">Subscribe For Our Newsletter</div>
  <div class="abs" style="left:894px;top:211px;width:150px;height:24px;background:#fff;color:#333;font-size:12px;padding:5px 8px;border-radius:12px 0 0 12px">Email Address</div>
  <div class="abs" style="left:1044px;top:211px;width:77px;height:24px;background:var(--yellow);font-size:12px;padding:5px 0;text-align:center;border-radius:0 12px 12px 0">Subscribe</div>
  <div class="abs" style="left:894px;top:254px;display:flex;gap:10px">
    <i style="display:block;width:24px;height:24px;border-radius:50%;background:#4a6aa5"></i>
    <i style="display:block;width:24px;height:24px;border-radius:50%;background:#3a7fb5"></i>
    <i style="display:block;width:24px;height:24px;border-radius:50%;background:#c23a2e"></i>
    <i style="display:block;width:24px;height:24px;border-radius:50%;background:#3aa1e0"></i>
  </div>

  <div class="abs" style="left:66px;top:324px;width:1068px;height:1px;background:#444"></div>
  <div class="abs" style="left:79px;top:343px;font-size:12px">CopyRight ©2018 K4 Logistic &amp; Plant Hire . All Right Reserve</div>
  <div class="abs" style="left:906px;top:343px;font-size:12px">Privacy Policy - Terms &amp; Conditions</div>
</footer>

</body>
</html>
```